Psychology practice - information brochure/flyer - half A4 page folded (4 sides)

We need a brochure/flyer to market our psychology service to GPs (Doctors). We need to demonstrate to the doctors that we are the right choice for their patients, and that we cover a large range of services so all of their patients needs are met. We will demonstrate this by listing our range of services and our team of psychologists. We have two locations in Sydney and offer high end services. I've attached our company logo but we remain flexible regarding the style of the brochures. I will provide more details (services, locations & psychologist credentials) once our preferred brochure design has been selected.

```html
<!DOCTYPE html>
<html lang="en">
<head>
<meta charset="utf-8">
<title>Psychology Practice Brochure – Inside Spread</title>
<link href="https://fonts.googleapis.com/css2?family=Ubuntu:wght@500;700&family=Open+Sans:wght@400;600&display=swap" rel="stylesheet">
<style>
  :root {
    --bg: #e3e3e3;
    --paper: #ffffff;
    --paper-soft: #f4f4f4;
    --charcoal: #444444;
    --accent: #f2b705;
    --text: #3a3a3a;
    --text-light: #f2f2f2;
    --rule: #555555;
    --photo-warm: #c9b8a6;
    --photo-cool: #9fa6ad;
  }
  * { box-sizing: border-box; margin: 0; padding: 0; }
  html, body { width: 1200px; height: 1003px; overflow: hidden; }
  body {
    background: var(--bg);
    font-family: "Open Sans", Arial, sans-serif;
    color: var(--text);
    position: relative;
  }
  .spread {
    position: absolute;
    left: 40px; top: 105px;
    width: 1120px; height: 792px;
    display: flex;
    box-shadow: 0 14px 30px rgba(0,0,0,.22);
  }
  .page {
    position: relative;
    width: 560px; height: 792px;
    background: linear-gradient(180deg, var(--paper), var(--paper-soft));
    overflow: hidden;
  }
  .page-left { border-right: 1px solid #d4d4d4; }
  .page-art { position: absolute; inset: 0; }

  /* section headings */
  .section-band {
    position: absolute;
    display: flex; align-items: center;
    background: var(--charcoal);
    color: var(--accent);
    font-family: "Ubuntu", Arial, sans-serif;
    font-weight: 700;
    font-size: 24px;
    padding-left: 22px;
  }
  .section-band::after {
    content: "";
    position: absolute;
    right: -16px; top: -10px;
    width: 18px; height: 30px;
    background: var(--accent);
    border-radius: 0 14px 0 14px;
  }
  .section-band.on-dark {
    background: var(--accent);
    color: var(--charcoal);
  }
  .section-band.on-dark::after { background: var(--paper); }

  .about-text {
    position: absolute;
    left: 24px; top: 300px; width: 260px;
    font-size: 12.5px; line-height: 19px;
    text-align: justify;
    hyphens: auto;
  }
  .bullet-list { list-style: none; position: absolute; }
  .bullet-list li { position: relative; padding-left: 16px; }
  .bullet-list li::before {
    content: "";
    position: absolute; left: 2px; top: 50%;
    width: 5px; height: 5px; margin-top: -2px;
    border-radius: 50%;
    background: var(--accent);
  }
  .client-list {
    left: 30px; top: 560px; width: 250px;
    font-size: 13px; line-height: 19px;
  }
  .service-list {
    left: 318px; top: 300px; width: 235px;
    font-size: 11.5px; line-height: 16.8px;
    color: var(--text-light);
  }

  /* clinicians */
  .clinician {
    position: absolute;
    display: flex; align-items: center; gap: 12px;
  }
  .clinician-photo {
    width: 70px; height: 64px; flex: none;
    background: linear-gradient(160deg, var(--photo-cool), var(--photo-warm));
  }
  .clinician-name {
    font-family: "Ubuntu", Arial, sans-serif;
    font-weight: 700; font-size: 12.5px;
    color: var(--accent);
  }
  .clinician-cred { font-size: 9.5px; line-height: 12px; color: var(--text); }

  /* fee table */
  .fee-table {
    position: absolute;
    left: 40px; top: 560px; width: 490px;
    border-collapse: collapse;
    font-size: 12.5px;
    text-align: center;
  }
  .fee-table th {
    background: var(--charcoal);
    color: var(--accent);
    font-family: "Ubuntu", Arial, sans-serif;
    font-weight: 500; font-size: 13.5px;
    height: 34px;
  }
  .fee-table td {
    height: 40px;
    border-bottom: 1px solid var(--rule);
    border-left: 1px solid var(--rule);
  }
  .fee-table td:first-child { border-left: none; }
  .fee-table tr:last-child td { border-bottom: none; }
  .fee-table td.time-cell { border-bottom: 1px solid var(--rule); }
</style>
</head>
<body>
<main class="spread">

  <!-- Left page -->
  <section class="page page-left">
    <svg class="page-art" width="560" height="792" viewBox="0 0 560 792" aria-hidden="false">
      <defs>
        <linearGradient id="sessionTone" x1="0" y1="0" x2="1" y2="1">
          <stop offset="0" stop-color="#d9d4cc"/>
          <stop offset=".55" stop-color="#b9a48f"/>
          <stop offset="1" stop-color="#e7e2dc"/>
        </linearGradient>
      </defs>
      <path role="img" aria-label="Photo of a client talking with a psychologist in a bright consulting room"
            d="M0,0 H560 V20 C460,120 360,180 290,200 C200,225 80,260 0,282 Z" fill="url(#sessionTone)"/>
      <path d="M0,282 C80,260 200,225 290,200 C360,180 460,120 560,20 V42 C470,140 380,200 300,226 C200,258 90,298 0,330 Z" fill="var(--accent)"/>
      <path d="M300,226 C380,200 470,140 560,42 V792 H300 Z" fill="var(--charcoal)"/>
    </svg>

    <h2 class="section-band" style="left:0; top:240px; width:270px; height:40px;">About Us</h2>
    <p class="about-text">We understand the factors that are contributing to and maintaining your difficulties and offer effective strategies to help you overcome and manage them. We are sensitive to the particular needs of our patients, thus, therapy is tailored to your individual needs using evidence-based treatments aimed at creating long-lasting change.</p>

    <h2 class="section-band" style="left:0; top:495px; width:270px; height:40px;">Our Client Groups</h2>
    <ul class="bullet-list client-list">
      <li>Children 5-12</li>
      <li>Adolescents</li>
      <li>Adults</li>
      <li>Veterans</li>
      <li>Victims of crime</li>
      <li>Injured workers</li>
      <li>Culturally and Linguistically Diverse backgrounds</li>
      <li>Refugees</li>
    </ul>

    <h2 class="section-band on-dark" style="left:300px; top:245px; width:230px; height:40px;">Our Services</h2>
    <ul class="bullet-list service-list">
      <li>Anxiety</li>
      <li>Depression</li>
      <li>Attention Deficit Hyperactivity Disorder (ADHD)</li>
      <li>Phobias</li>
      <li>Autism Spectrum Disorder</li>
      <li>Intellectual disability</li>
      <li>Learning difficulties</li>
      <li>Bullying</li>
      <li>Study stress</li>
      <li>Procrastination</li>
      <li>WorkCover</li>
      <li>Stress management</li>
      <li>Rehabilitation psychology</li>
      <li>Addiction and relapse prevention</li>
      <li>Anger management</li>
      <li>Divorce/separation</li>
      <li>Pregnancy</li>
      <li>Trauma</li>
      <li>Post-Traumatic Stress Disorder (PTSD)</li>
      <li>Couples/Family Therapy</li>
      <li>Domestic Violence</li>
      <li>Non-Suicidal Self Injury</li>
      <li>Grief and loss</li>
      <li>Eating disorders/body image</li>
    </ul>
  </section>

  <!-- Right page -->
  <section class="page page-right">
    <h2 class="section-band" style="left:0; top:55px; width:290px; height:42px;">Our Clinicians</h2>

    <div class="clinician" style="left:28px; top:150px;">
      <div class="clinician-photo" role="img" aria-label="Portrait photo of Dr Clara Menzies"></div>
      <div>
        <div class="clinician-name">Dr Clara Menzies</div>
        <div class="clinician-cred">DClinPsych, MA, BSc(Psych)<br>BPsych (Hons)</div>
      </div>
    </div>
    <div class="clinician" style="left:290px; top:120px;">
      <div class="clinician-photo" role="img" aria-label="Portrait photo of Dr Helena Varga"></div>
      <div>
        <div class="clinician-name">Dr Helena Varga</div>
        <div class="clinician-cred">D ClinPsych, MSc (Psych), B Psych (Hons)<br>MACPA, MAPS</div>
      </div>
    </div>
    <div class="clinician" style="left:28px; top:255px;">
      <div class="clinician-photo" role="img" aria-label="Portrait photo of Dr Thomas Edward Lowe"></div>
      <div>
        <div class="clinician-name">Dr Thomas Edward Lowe</div>
        <div class="clinician-cred">DPhil (Psych), BA-Psych (Hons)<br>GradDipEd, GDipMgt, MAPS, FCOP</div>
      </div>
    </div>
    <div class="clinician" style="left:290px; top:225px;">
      <div class="clinician-photo" role="img" aria-label="Portrait photo of Nadia Petrosyan"></div>
      <div>
        <div class="clinician-name">Nadia Petrosyan</div>
        <div class="clinician-cred">MPsych (Clin), BPsych (Hons)</div>
      </div>
    </div>
    <div class="clinician" style="left:28px; top:355px;">
      <div class="clinician-photo" role="img" aria-label="Portrait photo of Sana Qureshi"></div>
      <div>
        <div class="clinician-name">Sana Qureshi</div>
        <div class="clinician-cred">BPsych (Hons), GDipPsych</div>
      </div>
    </div>

    <h2 class="section-band" style="left:0; top:470px; width:320px; height:46px; font-size:27px;">Our Fee Structure</h2>

    <table class="fee-table">
      <thead>
        <tr><th>Time</th><th>Fee/Per Session</th><th>Psychologist</th><th>Medicare Rebate</th></tr>
      </thead>
      <tbody>
        <tr><td class="time-cell" rowspan="2">9am to 5 pm</td><td>$150</td><td>General Psychologist</td><td>$84.80</td></tr>
        <tr><td>$190</td><td>Clinical Psychologist</td><td>$124.50</td></tr>
        <tr><td class="time-cell" rowspan="2">After 5pm</td><td>$170</td><td>General Psychologist</td><td>$84.80</td></tr>
        <tr><td>$210</td><td>Clinical Psychologist</td><td>$124.50</td></tr>
      </tbody>
    </table>
  </section>

</main>
</body>
</html>
```